Washington DC Solo Practitioner Law Firm needs Stationery and Business Card Design

We need a letterhead and business card for a new law firm based in Washington DC called Harlow PLLC. The law firm is a single lawyer practicing appellate law (U.S. Supreme Court, Federal District Courts, State Supreme Courts).
We already have a logo designed through a MarkHive contest. The letterhead and the business card should include the Logo and have the same look and feel as the Logo - same fonts and colors, please. We would like a clean, crisp, simple, professional look. The design should convey stability and experience.
We have .png and .psd and .ai files for the logo, as needed
Dark blue color is PANTONE P 108-16 C
Grey color is PANTONE P 179-11 C
Type face is Century Gothic Regular typeface

```html
<!DOCTYPE html>
<html lang="en">
<head>
<meta charset="utf-8">
<title>Harlow PLLC – Business Card</title>
<link href="https://fonts.googleapis.com/css2?family=Questrial&display=swap" rel="stylesheet">
<style>
  :root {
    --page: #ffffff;
    --band-light: #bfbfbf;
    --band-mid: #6a6a6a;
    --band-dark: #000000;
    --navy: #0b3a6b;
    --label-red: #c0001f;
    --tagline: #d6d6d6;
  }
  html, body {
    margin: 0;
    padding: 0;
    width: 1200px;
    height: 900px;
    overflow: hidden;
    background: var(--page);
    font-family: "Questrial", "Century Gothic", sans-serif;
  }
  .canvas {
    position: relative;
    width: 1200px;
    height: 900px;
  }
  .card-band {
    position: absolute;
    left: 0;
    top: 150px;
    width: 1200px;
    height: 600px;
    background: linear-gradient(
      to bottom,
      var(--band-light) 0px,
      var(--band-light) 185px,
      var(--band-mid) 330px,
      #1a1a1a 470px,
      var(--band-dark) 540px
    );
  }
  .side-label {
    position: absolute;
    top: 160px;
    margin: 0;
    font-size: 29px;
    font-style: italic;
    color: var(--label-red);
    transform: translateX(-50%);
  }
  .side-label.front { left: 368px; }
  .side-label.back { left: 903px; }

  .brand-square {
    position: absolute;
    left: 70px;
    top: 370px;
    width: 80px;
    height: 80px;
    background: var(--navy);
  }
  .firm-name {
    position: absolute;
    left: 175px;
    top: 360px;
    margin: 0;
    font-size: 82px;
    font-weight: 400;
    color: var(--navy);
    line-height: 1;
    white-space: nowrap;
  }
  .tagline {
    position: absolute;
    left: 255px;
    top: 545px;
    width: 336px;
    margin: 0;
    font-size: 33px;
    letter-spacing: -1.5px;
    color: var(--tagline);
    text-align: center;
    white-space: nowrap;
  }
  .contact {
    position: absolute;
    left: 911px;
    top: 350px;
    margin: 0;
    transform: translateX(-50%);
    text-align: center;
    font-style: italic;
    font-size: 34px;
    line-height: 50px;
    letter-spacing: -1px;
    color: var(--navy);
    white-space: nowrap;
  }
  .contact span { display: block; }
</style>
</head>
<body>
  <main class="canvas">
    <section class="card-band">
    </section>

    <p class="side-label front">Front</p>
    <p class="side-label back">Back</p>

    <div class="brand-square" aria-hidden="true"></div>
    <h1 class="firm-name">Harlow PLLC</h1>
    <p class="tagline">TRIAL AND APPELLATE LITIGATION</p>

    <address class="contact">
      <span>Name</span>
      <span>Address</span>
      <span>Phone Number</span>
      <span>Email Address</span>
    </address>
  </main>
</body>
</html>
```